shutter business card and postcard design

Custom Interior and Exterior Shutters manufactured In Houston Texas Made in USA we offer fast delivery lifetime warranty
Dean Whitfield owner has been manufacturing shutters in houston for over 44 years
nedd to use one of the pictures provided and add company name phone number on face Louver Loft (281)555-0187
back side
louver loft
8217 calloway ln.
houston, texas 77099
email louverloft@examplemail.test
website louverlofthouston.test

Industry/Entity Type

Business

```html
<!DOCTYPE html>
<html lang="en">
<head>
<meta charset="utf-8">
<title>Louver Loft Postcard</title>
<link rel="stylesheet" href="https://fonts.googleapis.com/css2?family=Montserrat:wght@700&family=Oswald:wght@500;600&family=Questrial&display=swap">
<style>
  :root {
    --brown: #4b1d15;
    --brown-dark: #351009;
    --orange: #f7a51c;
    --orange-deep: #ef8a12;
    --ink: #2b1a16;
    --panel: #ececec;
    --white: #ffffff;
    --stage: #3b3b3b;
  }
  * { margin: 0; padding: 0; box-sizing: border-box; }
  html, body { width: 848px; height: 1200px; overflow: hidden; }
  body { background: var(--stage); position: relative; font-family: "Questrial", sans-serif; }

  .card { position: absolute; left: 26px; width: 796px; height: 536px; background: var(--white); overflow: hidden; }
  .card--front { top: 48px; }
  .card--back { top: 616px; }
  .card-art { position: absolute; inset: 0; width: 796px; height: 536px; }
  .abs { position: absolute; }
  .condensed { white-space: nowrap; transform-origin: left top; font-family: "Oswald", sans-serif; font-weight: 600; }

  /* front */
  .brand-title { left: 28px; top: 24px; font-family: "Montserrat", sans-serif; font-weight: 700; font-size: 44px; color: var(--orange); letter-spacing: 0.5px; white-space: nowrap; }
  .brand-tagline { left: 28px; top: 82px; font-size: 27px; line-height: 34px; color: var(--white); }
  .product-line { left: 28px; top: 322px; font-size: 29px; color: var(--ink); transform: scaleX(0.74); }
  .origin-line { left: 28px; top: 348px; font-size: 38px; color: var(--brown); transform: scaleX(0.72); }
  .made-usa { left: 28px; top: 404px; width: 380px; display: flex; align-items: center; gap: 14px; font-size: 22px; letter-spacing: 4px; color: var(--ink); white-space: nowrap; }
  .made-usa::before, .made-usa::after { content: ""; flex: 1; height: 1.5px; background: var(--ink); }
  .owner-note { left: 28px; top: 442px; width: 430px; font-size: 15.5px; line-height: 20px; color: var(--ink); }
  .perk { top: 366px; width: 130px; text-align: center; font-family: "Oswald", sans-serif; font-weight: 500; font-size: 19px; line-height: 23px; color: var(--ink); letter-spacing: 0.5px; }
  .perk--delivery { left: 507px; }
  .perk--warranty { left: 643px; }
  .call-us { left: 537px; top: 428px; font-size: 34px; color: var(--white); transform: scaleX(0.7); }

  /* back */
  .about-title { left: 28px; top: 171px; font-family: "Montserrat", sans-serif; font-weight: 700; font-size: 23px; color: var(--brown); }
  .about-copy { left: 28px; top: 209px; width: 400px; font-size: 16.5px; line-height: 19.5px; color: var(--ink); }
  .about-copy p + p { margin-top: 6px; }
  .appointment { left: 28px; top: 352px; font-size: 27px; color: var(--brown-dark); transform: scaleX(0.72); }
  .back-brand { left: 28px; top: 409px; font-family: "Montserrat", sans-serif; font-weight: 700; font-size: 23px; color: var(--orange); }
  .contact-list { left: 28px; top: 443px; list-style: none; font-size: 15px; color: var(--white); }
  .contact-list li { display: flex; align-items: center; gap: 10px; height: 24px; }
  .contact-list svg { width: 14px; height: 14px; flex: none; }
  .stamp-box { left: 675px; top: 30px; width: 88px; height: 87px; border: 1.5px solid #222; }
  .address-line { left: 518px; width: 244px; height: 1.5px; background: #222; }
</style>
</head>
<body>

<section class="card card--front">
  <svg class="card-art" viewBox="0 0 796 536">
    <defs>
      <linearGradient id="brownFill" x1="0" y1="0" x2="1" y2="1">
        <stop offset="0" stop-color="#5a2419"/><stop offset="1" stop-color="#3a120b"/>
      </linearGradient>
      <linearGradient id="panelFill" x1="0" y1="0" x2="0" y2="1">
        <stop offset="0" stop-color="#f4f4f4"/><stop offset="1" stop-color="#dcdcdc"/>
      </linearGradient>
      <linearGradient id="diningPhoto" x1="0" y1="0" x2="1" y2="1">
        <stop offset="0" stop-color="#5f625f"/><stop offset="0.5" stop-color="#a39d94"/><stop offset="1" stop-color="#6b5a4a"/>
      </linearGradient>
      <linearGradient id="windowPhoto" x1="0" y1="0" x2="1" y2="0">
        <stop offset="0" stop-color="#f3f2ee"/><stop offset="0.6" stop-color="#e6e0d6"/><stop offset="1" stop-color="#d8cfc2"/>
      </linearGradient>
      <clipPath id="frontRight"><path d="M472 0 Q420 250 528 488 L796 488 L796 0 Z"/></clipPath>
    </defs>

    <rect x="0" y="0" width="796" height="536" fill="url(#panelFill)"/>
    <rect x="0" y="0" width="480" height="166" fill="url(#brownFill)"/>
    <g role="img" aria-label="Photo of a dining room with plantation shutters on tall windows">
      <rect x="0" y="166" width="470" height="146" fill="url(#diningPhoto)"/>
    </g>

    <g clip-path="url(#frontRight)">
      <g role="img" aria-label="Photo of a woman opening white plantation shutters at a sunny window">
        <rect x="420" y="0" width="376" height="331" fill="url(#windowPhoto)"/>
      </g>
      <rect x="420" y="331" width="376" height="90" fill="url(#panelFill)"/>
      <rect x="420" y="331" width="376" height="4" fill="var(--brown)"/>
      <rect x="420" y="421" width="376" height="67" fill="url(#brownFill)"/>
    </g>
    <path d="M472 0 Q420 250 528 488" fill="none" stroke="#fff" stroke-width="6"/>
    <path d="M458 0 Q404 250 512 492" fill="none" stroke="var(--orange)" stroke-width="14"/>

    <rect x="0" y="486" width="796" height="12" fill="var(--orange)"/>
    <rect x="0" y="498" width="796" height="38" fill="url(#brownFill)"/>

    <circle cx="572" cy="335" r="23" fill="var(--brown)"/>
    <g fill="var(--orange)">
      <rect x="556" y="327" width="18" height="13" rx="1"/>
      <path d="M575 331 h7 l5 5 v4 h-12 z"/>
      <circle cx="561" cy="342" r="3"/><circle cx="581" cy="342" r="3"/>
    </g>
    <circle cx="708" cy="335" r="23" fill="var(--brown)"/>
    <g fill="none" stroke="var(--orange)" stroke-width="2">
      <rect x="698" y="323" width="18" height="22" rx="1"/>
      <path d="M702 329 h10 M702 334 h10"/>
    </g>
    <circle cx="713" cy="343" r="4" fill="var(--orange)"/>
  </svg>

  <h1 class="abs brand-title">LOUVER LOFT</h1>
  <p class="abs brand-tagline">LEADING MANUFACTURER<br>OF PLANTATION SHUTTERS</p>
  <p class="abs condensed product-line">CUSTOM INTERIOR AND EXTERIOR SHUTTERS</p>
  <p class="abs condensed origin-line">MANUFACTURED IN HOUSTON TEXAS</p>
  <p class="abs made-usa">MADE IN USA</p>
  <p class="abs owner-note">Dean Whitfield owner has been manufacturing shutters in houston for over 44 years</p>
  <p class="abs perk perk--delivery">FAST<br>DELIVERY</p>
  <p class="abs perk perk--warranty">LIFETIME<br>WARRANTY</p>
  <p class="abs condensed call-us">CALL US: (281)555-0187</p>
</section>

<section class="card card--back">
  <svg class="card-art" viewBox="0 0 796 536">
    <defs>
      <linearGradient id="officePhoto" x1="0" y1="0" x2="0" y2="1">
        <stop offset="0" stop-color="#5d645d"/><stop offset="0.55" stop-color="#8e8a7e"/><stop offset="1" stop-color="#f2f2f2"/>
      </linearGradient>
      <linearGradient id="backPanel" x1="0" y1="0" x2="0" y2="1">
        <stop offset="0" stop-color="#f4f4f4"/><stop offset="1" stop-color="#e2e2e2"/>
      </linearGradient>
      <linearGradient id="backBrown" x1="0" y1="0" x2="1" y2="1">
        <stop offset="0" stop-color="#5a2419"/><stop offset="1" stop-color="#3a120b"/>
      </linearGradient>
      <clipPath id="backLeft"><path d="M0 0 L396 0 Q540 270 336 536 L0 536 Z"/></clipPath>
    </defs>

    <path d="M396 0 Q540 270 336 536" fill="none" stroke="var(--orange)" stroke-width="44" transform="translate(14 0)"/>
    <path d="M396 0 Q540 270 336 536" fill="none" stroke="var(--brown)" stroke-width="28"/>
    <g clip-path="url(#backLeft)">
      <rect x="0" y="0" width="500" height="536" fill="url(#backPanel)"/>
      <g role="img" aria-label="Photo of a home office with arched windows fitted with plantation shutters">
        <rect x="0" y="0" width="500" height="170" fill="url(#officePhoto)"/>
      </g>
      <rect x="0" y="345" width="500" height="55" fill="var(--orange)"/>
      <rect x="0" y="400" width="500" height="136" fill="url(#backBrown)"/>
    </g>
  </svg>

  <h2 class="abs about-title">ABOUT US</h2>
  <div class="abs about-copy">
    <p>For more than a decade Louver Loft has been a leading manufacturer of plantation shutters lenders payday loans in the Houston area.</p>
    <p>After you make an appointment, our staff will come to your home to make precise measurements of each window.</p>
  </div>
  <p class="abs condensed appointment">CALL TODAY FOR AN APPOINTMENT!: (281)555-0187</p>
  <h2 class="abs back-brand">LOUVER LOFT</h2>
  <ul class="abs contact-list">
    <li><svg viewBox="0 0 14 14"><path d="M7 1 L1 7 H3 V13 H6 V9 H8 V13 H11 V7 H13 Z" fill="#f7a51c"/></svg>8217 calloway ln. houston, texas 77099</li>
    <li><svg viewBox="0 0 14 14"><rect x="1" y="3" width="12" height="8" fill="#f7a51c"/><path d="M1 3 L7 8 L13 3" fill="none" stroke="#4b1d15" stroke-width="1.2"/></svg>louverloft@examplemail.test</li>
    <li><svg viewBox="0 0 14 14"><circle cx="7" cy="7" r="6" fill="#f7a51c"/><path d="M1 7 H13 M7 1 V13 M3 3.5 Q7 6 11 3.5 M3 10.5 Q7 8 11 10.5" fill="none" stroke="#4b1d15" stroke-width="0.8"/></svg>www.louverlofthouston.test</li>
  </ul>

  <div class="abs stamp-box"></div>
  <div class="abs address-line" style="top:332px"></div>
  <div class="abs address-line" style="top:374px"></div>
  <div class="abs address-line" style="top:416px"></div>
</section>

</body>
</html>
```